Election Results Powerpoint

Hello!
I'm in need of a way to display election results for multiple students' union elections. My thinking is a Powerpoint template which can be easily edited/updated, however if you can think of another way that this could be done which doesn't require specialist software I'm open to suggestions.
The display must be able to accommodate demonstrating an 'Alternative Vote' election (http://www.qorvex.co.uk/news/uk-politics-48157203). Several candidates may stand for one position, and the display must accommodate being able to show a picture of each candidate, transfer of votes from an eliminated candidate to other candidates and be able to show the 'quota' for each round until we have a winner.
The display must be simple to understand for someone who has no prior knowledge of elections & if possible be exciting in its presentation. These results will be displayed to a large crowd and will be the method for people to find out if their candidate has won.
I have attached the logo of the organisation which must be included in the design.
A possible example of what you need to aim for is here - http://www.vidlumo.com/watch?v=Kp7TRbNxQaL&t=91m0s - But I'm sure you lovely people out there can do better :)
Thanks

```html
<!DOCTYPE html>
<html lang="en">
<head>
<meta charset="utf-8">
<title>Election Results – Round 02</title>
<link rel="stylesheet" href="https://fonts.googleapis.com/css2?family=Carlito:wght@400;700&family=Open+Sans:wght@400;600&display=swap">
<style>
  :root {
    --backdrop: #7f7f7f;
    --slide-top: #ffffff;
    --slide-bottom: #ececec;
    --brand-red: #c8202a;
    --cap-red: #d0504f;
    --ink: #222222;
    --axis: #9a9a9a;
    --rule: #d2d2d2;
    --alessandro: #fdc96a;
    --roberto: #8ed34a;
    --pietro: #4f8fd6;
    --andrea: #c8be96;
    --gustavo: #c4c4c4;
  }
  * { box-sizing: border-box; margin: 0; padding: 0; }
  html, body { width: 1022px; height: 1200px; overflow: hidden; }
  body { background: var(--backdrop); position: relative; font-family: "Carlito", "Calibri", sans-serif; color: var(--ink); }

  .slide {
    position: absolute; left: 48px; width: 938px; height: 525px;
    background: linear-gradient(180deg, var(--slide-top) 0%, var(--slide-bottom) 100%);
    overflow: hidden;
  }
  .slide--first { top: 41px; }
  .slide--second { top: 607px; }

  .chart { position: absolute; left: 0; top: 0; width: 938px; height: 525px; }

  .round-bar { position: absolute; left: 3px; top: 16px; width: 4px; height: 58px; background: var(--brand-red); }
  .round-title { position: absolute; left: 11px; top: 17px; font-family: "Open Sans", sans-serif; font-size: 40px; line-height: 48px; color: var(--brand-red); letter-spacing: -0.5px; }
  .round-number { position: absolute; left: 147px; top: 17px; width: 55px; height: 55px; border-radius: 50%; background: var(--brand-red); color: #fff; font-family: "Open Sans", sans-serif; font-weight: 600; font-size: 25px; line-height: 55px; text-align: center; }
  .header-rule { position: absolute; left: 238px; top: 0; width: 1px; height: 76px; background: var(--rule); }

  .stat { position: absolute; left: 250px; width: 300px; height: 26px; display: flex; justify-content: flex-end; align-items: center; gap: 8px; }
  .stat--polled { top: 32px; }
  .stat--transfer { top: 75px; }
  .stat-label { font-size: 21px; color: var(--ink); }
  .stat-value { width: 66px; height: 26px; background: var(--brand-red); color: #fff; font-size: 19px; line-height: 26px; text-align: center; }

  .brand { position: absolute; left: 828px; top: 0; width: 81px; height: 78px; background: #fff; box-shadow: 2px 3px 5px rgba(0,0,0,0.35); display: flex; flex-direction: column; align-items: center; justify-content: center; gap: 4px; }
  .brand-dot { width: 22px; height: 22px; border-radius: 50%; background: var(--brand-red); }
  .brand-name { font-size: 10px; line-height: 11px; color: var(--brand-red); text-align: center; font-weight: 700; }

  .eliminated-tab { position: absolute; left: 776px; top: 110px; width: 137px; height: 23px; background: var(--brand-red); color: #fff; font-size: 16px; line-height: 23px; padding-left: 14px; }
  .eliminated-rule { position: absolute; left: 784px; top: 133px; width: 2px; height: 356px; background: var(--rule); }

  .footer { position: absolute; left: 0; bottom: 0; width: 938px; height: 17px; background: var(--brand-red); color: #fff; font-size: 9.5px; font-weight: 700; line-height: 17px; text-transform: uppercase; display: flex; justify-content: space-between; padding: 0 14px; }

  .axis-label { font-family: "Carlito", sans-serif; font-size: 10px; fill: var(--ink); }
  .name-label { font-family: "Carlito", sans-serif; font-size: 10px; fill: var(--ink); }
  .bar-value { font-family: "Carlito", sans-serif; font-size: 10px; fill: var(--ink); }
  .portrait-ring { fill: #fff; stroke: #d8d8d8; stroke-width: 1; }
</style>
</head>
<body>

<!-- Round 02: votes with transfers shown -->
<section class="slide slide--first">
  <svg class="chart" viewBox="0 0 683 382" aria-label="Bar chart of votes per candidate with transferred votes">
    <defs>
      <radialGradient id="portrait-tone-a" cx="50%" cy="40%" r="60%">
        <stop offset="0" stop-color="#e7c2a5"/><stop offset="1" stop-color="#7d6b5f"/>
      </radialGradient>
      <radialGradient id="portrait-tone-b" cx="50%" cy="40%" r="60%">
        <stop offset="0" stop-color="#c9a88e"/><stop offset="1" stop-color="#3c4a58"/>
      </radialGradient>
      <radialGradient id="portrait-tone-c" cx="50%" cy="40%" r="60%">
        <stop offset="0" stop-color="#f1dcc0"/><stop offset="1" stop-color="#b49a6e"/>
      </radialGradient>
    </defs>

    <g class="y-axis">
      <line x1="77" y1="104" x2="77" y2="330" stroke="var(--axis)" stroke-width="0.8"/>
      <text class="axis-label" x="66" y="333.5" text-anchor="end">0</text>
      <text class="axis-label" x="66" y="310.9" text-anchor="end">100</text>
      <text class="axis-label" x="66" y="288.3" text-anchor="end">200</text>
      <text class="axis-label" x="66" y="265.7" text-anchor="end">300</text>
      <text class="axis-label" x="66" y="243.1" text-anchor="end">400</text>
      <text class="axis-label" x="66" y="220.5" text-anchor="end">500</text>
      <text class="axis-label" x="66" y="197.9" text-anchor="end">600</text>
      <text class="axis-label" x="66" y="175.3" text-anchor="end">700</text>
      <text class="axis-label" x="66" y="152.7" text-anchor="end">800</text>
      <text class="axis-label" x="66" y="130.1" text-anchor="end">900</text>
      <text class="axis-label" x="66" y="107.5" text-anchor="end">1000</text>
    </g>
    <line class="quota-line" x1="77" y1="126.6" x2="566" y2="126.6" stroke="var(--brand-red)" stroke-width="1" stroke-dasharray="4 3"/>
    <g class="x-axis" stroke="var(--axis)" stroke-width="0.8">
      <line x1="77" y1="330" x2="553" y2="330"/>
      <line x1="77" y1="330" x2="77" y2="334"/>
      <line x1="172" y1="330" x2="172" y2="334"/>
      <line x1="267" y1="330" x2="267" y2="334"/>
      <line x1="362" y1="330" x2="362" y2="334"/>
      <line x1="457" y1="330" x2="457" y2="334"/>
      <line x1="553" y1="330" x2="553" y2="334"/>
    </g>

    <!-- bars -->
    <rect x="104" y="183.1" width="42" height="146.9" fill="var(--alessandro)"/>
    <rect x="104" y="176.3" width="42" height="6.8" fill="var(--cap-red)"/>
    <rect x="199" y="284.8" width="42" height="45.2" fill="var(--roberto)"/>
    <rect x="199" y="280.3" width="42" height="4.5" fill="var(--cap-red)"/>
    <rect x="294" y="284.8" width="42" height="45.2" fill="var(--pietro)"/>
    <rect x="294" y="281.4" width="42" height="3.4" fill="var(--cap-red)"/>
    <rect x="389" y="217" width="42" height="113" fill="var(--andrea)"/>
    <rect x="389" y="212.5" width="42" height="4.5" fill="var(--cap-red)"/>
    <rect x="484" y="296.1" width="42" height="33.9" fill="var(--gustavo)"/>
    <rect x="484" y="292.7" width="42" height="3.4" fill="var(--cap-red)"/>

    <g class="bar-values" text-anchor="middle">
      <text class="bar-value" x="125" y="324">650</text>
      <text class="bar-value" x="125" y="194">30</text>
      <text class="bar-value" x="220" y="324">200</text>
      <text class="bar-value" x="220" y="295">20</text>
      <text class="bar-value" x="315" y="324">200</text>
      <text class="bar-value" x="315" y="295">15</text>
      <text class="bar-value" x="410" y="324">500</text>
      <text class="bar-value" x="410" y="228">20</text>
      <text class="bar-value" x="505" y="324">150</text>
      <text class="bar-value" x="505" y="306">15</text>
    </g>

    <g class="portraits">
      <g role="img" aria-label="Portrait of Alessandro"><circle class="portrait-ring" cx="128" cy="157" r="25"/><circle cx="128" cy="157" r="21.5" fill="url(#portrait-tone-a)"/></g>
      <g role="img" aria-label="Portrait of Roberto"><circle class="portrait-ring" cx="220" cy="257" r="25"/><circle cx="220" cy="257" r="21.5" fill="url(#portrait-tone-b)"/></g>
      <g role="img" aria-label="Portrait of Pietro"><circle class="portrait-ring" cx="315" cy="257" r="25"/><circle cx="315" cy="257" r="21.5" fill="url(#portrait-tone-b)"/></g>
      <g role="img" aria-label="Portrait of Andrea"><circle class="portrait-ring" cx="410" cy="191" r="25"/><circle cx="410" cy="191" r="21.5" fill="url(#portrait-tone-a)"/></g>
      <g role="img" aria-label="Portrait of Gustavo"><circle class="portrait-ring" cx="505" cy="270" r="25"/><circle cx="505" cy="270" r="21.5" fill="url(#portrait-tone-a)"/></g>
      <g role="img" aria-label="Portrait of the eliminated candidate"><circle class="portrait-ring" cx="618" cy="135" r="25"/><circle cx="618" cy="135" r="21.5" fill="url(#portrait-tone-c)"/></g>
    </g>

    <g class="names" text-anchor="middle">
      <text class="name-label" x="125" y="350">Alessandro</text>
      <text class="name-label" x="220" y="350">Roberto</text>
      <text class="name-label" x="315" y="350">Pietro</text>
      <text class="name-label" x="410" y="350">Andrea</text>
      <text class="name-label" x="505" y="350">Gustavo</text>
    </g>
  </svg>

  <div class="round-bar"></div>
  <div class="round-title">ROUND</div>
  <div class="round-number">02</div>
  <div class="header-rule"></div>
  <div class="stat stat--polled"><span class="stat-label">Number of Votes polled</span><span class="stat-value">1800</span></div>
  <div class="stat stat--transfer"><span class="stat-label">Number of Votes transfer</span><span class="stat-value">100</span></div>
  <div class="brand"><span class="brand-dot"></span><span class="brand-name">Harrowgate Vale<br>Students Union</span></div>
  <div class="eliminated-tab">Eliminated</div>
  <div class="eliminated-rule"></div>
  <footer class="footer"><span>Harrowgate Vale Students Union</span><span>Election Results 2014</span></footer>
</section>

<!-- Round 02: combined totals -->
<section class="slide slide--second">
  <svg class="chart" viewBox="0 0 683 382" aria-label="Bar chart of total votes per candidate">
    <defs>
      <radialGradient id="portrait-tone-d" cx="50%" cy="40%" r="60%">
        <stop offset="0" stop-color="#e7c2a5"/><stop offset="1" stop-color="#7d6b5f"/>
      </radialGradient>
      <radialGradient id="portrait-tone-e" cx="50%" cy="40%" r="60%">
        <stop offset="0" stop-color="#c9a88e"/><stop offset="1" stop-color="#3c4a58"/>
      </radialGradient>
      <radialGradient id="portrait-tone-f" cx="50%" cy="40%" r="60%">
        <stop offset="0" stop-color="#f1dcc0"/><stop offset="1" stop-color="#b49a6e"/>
      </radialGradient>
    </defs>

    <g class="y-axis">
      <line x1="77" y1="104" x2="77" y2="330" stroke="var(--axis)" stroke-width="0.8"/>
      <text class="axis-label" x="66" y="333.5" text-anchor="end">0</text>
      <text class="axis-label" x="66" y="310.9" text-anchor="end">100</text>
      <text class="axis-label" x="66" y="288.3" text-anchor="end">200</text>
      <text class="axis-label" x="66" y="265.7" text-anchor="end">300</text>
      <text class="axis-label" x="66" y="243.1" text-anchor="end">400</text>
      <text class="axis-label" x="66" y="220.5" text-anchor="end">500</text>
      <text class="axis-label" x="66" y="197.9" text-anchor="end">600</text>
      <text class="axis-label" x="66" y="175.3" text-anchor="end">700</text>
      <text class="axis-label" x="66" y="152.7" text-anchor="end">800</text>
      <text class="axis-label" x="66" y="130.1" text-anchor="end">900</text>
      <text class="axis-label" x="66" y="107.5" text-anchor="end">1000</text>
    </g>
    <line class="quota-line" x1="77" y1="126.6" x2="566" y2="126.6" stroke="var(--brand-red)" stroke-width="1" stroke-dasharray="4 3"/>
    <g class="x-axis" stroke="var(--axis)" stroke-width="0.8">
      <line x1="77" y1="330" x2="553" y2="330"/>
      <line x1="77" y1="330" x2="77" y2="334"/>
      <line x1="172" y1="330" x2="172" y2="334"/>
      <line x1="267" y1="330" x2="267" y2="334"/>
      <line x1="362" y1="330" x2="362" y2="334"/>
      <line x1="457" y1="330" x2="457" y2="334"/>
      <line x1="553" y1="330" x2="553" y2="334"/>
    </g>

    <rect x="104" y="176.3" width="42" height="153.7" fill="var(--alessandro)"/>
    <rect x="199" y="280.3" width="42" height="49.7" fill="var(--roberto)"/>
    <rect x="294" y="281.4" width="42" height="48.6" fill="var(--pietro)"/>
    <rect x="389" y="212.5" width="42" height="117.5" fill="var(--andrea)"/>
    <rect x="484" y="292.7" width="42" height="37.3" fill="var(--gustavo)"/>

    <g class="bar-values" text-anchor="middle">
      <text class="bar-value" x="125" y="256">680</text>
      <text class="bar-value" x="220" y="310">220</text>
      <text class="bar-value" x="315" y="310">215</text>
      <text class="bar-value" x="410" y="269">520</text>
      <text class="bar-value" x="505" y="316">165</text>
    </g>

    <g class="portraits">
      <g role="img" aria-label="Portrait of Alessandro"><circle class="portrait-ring" cx="128" cy="157" r="25"/><circle cx="128" cy="157" r="21.5" fill="url(#portrait-tone-d)"/></g>
      <g role="img" aria-label="Portrait of Roberto"><circle class="portrait-ring" cx="220" cy="257" r="25"/><circle cx="220" cy="257" r="21.5" fill="url(#portrait-tone-e)"/></g>
      <g role="img" aria-label="Portrait of Pietro"><circle class="portrait-ring" cx="315" cy="257" r="25"/><circle cx="315" cy="257" r="21.5" fill="url(#portrait-tone-e)"/></g>
      <g role="img" aria-label="Portrait of Andrea"><circle class="portrait-ring" cx="410" cy="191" r="25"/><circle cx="410" cy="191" r="21.5" fill="url(#portrait-tone-d)"/></g>
      <g role="img" aria-label="Portrait of Gustavo"><circle class="portrait-ring" cx="505" cy="270" r="25"/><circle cx="505" cy="270" r="21.5" fill="url(#portrait-tone-d)"/></g>
      <g role="img" aria-label="Portrait of the eliminated candidate"><circle class="portrait-ring" cx="618" cy="135" r="25"/><circle cx="618" cy="135" r="21.5" fill="url(#portrait-tone-f)"/></g>
    </g>

    <g class="names" text-anchor="middle">
      <text class="name-label" x="125" y="350">Alessandro</text>
      <text class="name-label" x="220" y="350">Roberto</text>
      <text class="name-label" x="315" y="350">Pietro</text>
      <text class="name-label" x="410" y="350">Andrea</text>
      <text class="name-label" x="505" y="350">Gustavo</text>
    </g>
  </svg>

  <div class="round-bar"></div>
  <div class="round-title">ROUND</div>
  <div class="round-number">02</div>
  <div class="header-rule"></div>
  <div class="stat stat--polled"><span class="stat-label">Number of Votes polled</span><span class="stat-value">1800</span></div>
  <div class="stat stat--transfer"><span class="stat-label">Number of Votes transfer</span><span class="stat-value">100</span></div>
  <div class="brand"><span class="brand-dot"></span><span class="brand-name">Harrowgate Vale<br>Students Union</span></div>
  <div class="eliminated-tab">Eliminated</div>
  <div class="eliminated-rule"></div>
  <footer class="footer"><span>Harrowgate Vale Students Union</span><span>Election Results 2014</span></footer>
</section>

</body>
</html>
```